A New and modern Business Card for Talvern Contract Partners Ltd

New and modern Logo and Business Card Attached is the current logo/business card designCurrently the business is called "Talvern & Co." or TCP Ltd for short. This is subject to change.This business specialises in Telecoms and Energy. We work with the major networks (KX, V7, etc) and also offer Energy Products saving clients money off their energy bills.These are business to business services.The current design incorporates a Pheonix, indicating rebirth, starting something new.We would like to maintain the Phoenix element but a newer modern style.We love colours in the logo 3 max.The aim of this is to be ultra slick and modern. I envisage Talvern & Co. on one side of the card with long descriptions on the other side.Side 1:TCP Ltd/Logo?Side 2:TCP Ltd/Logo/Graphic?Brogan & Co.Name:Address:Phone:Email:The design is mostly flexible but must incorporate a Phoenix.For example "Talvern & Co." with a block phoenix behind the text...up to you.

Industry/Entity Type

Telecommunications

Contact Information for Business Card

Talvern & Co.
Address:
Name:
Phone:
Email:

Logo Text

Talvern & Co.

Colors
33a6d7
0792cd
acd037
9bcb3c
f78f20
fece3e

Requirements
Must have
• Phoenix
• 3/4 colours max
• Blue representing Technology (wireless)
• Green for Eco Energy
• Orange for Phoenix
• White business card background
Should not have
• phoenix must not all be red/ orange fire, we are a technology service company and the phoenix colours must represent this. Fire is not representative of our company.

```html
<!DOCTYPE html>
<html lang="en">
<head>
<meta charset="utf-8">
<title>Talvern &amp; Co. Business Card</title>
<link rel="stylesheet" href="https://fonts.googleapis.com/css2?family=Oswald:wght@600&family=Work+Sans:wght@400;500&display=swap">
<style>
  :root {
    --stage: #1c1c1c;
    --card-dark: #232323;
    --card-light: #ffffff;
    --ink: #3f3f3f;
    --ink-soft: #555555;
    --brand-blue: #1f3f93;
    --brand-orange: #f7a240;
    --logo-light: #f2f2f2;
  }
  html, body {
    margin: 0;
    padding: 0;
    width: 1200px;
    height: 900px;
    overflow: hidden;
    background: var(--stage);
  }
  .stage {
    position: relative;
    width: 1200px;
    height: 900px;
  }
  .card {
    position: absolute;
    left: 290px;
    width: 620px;
    height: 354px;
    box-sizing: border-box;
    box-shadow: 0 14px 30px rgba(0,0,0,.55);
  }
  .card--back {
    top: 56px;
    background: var(--card-dark);
    display: flex;
    align-items: center;
    justify-content: center;
  }
  .card--front {
    top: 470px;
    background: var(--card-light);
    font-family: "Work Sans", sans-serif;
    color: var(--ink);
  }
  .wordmark {
    display: flex;
    align-items: center;
    gap: 14px;
    font-family: "Work Sans", sans-serif;
    font-weight: 400;
    letter-spacing: 1px;
  }
  .wordmark__square {
    width: 22px;
    height: 22px;
    background: var(--brand-orange);
  }
  .card--back .wordmark {
    font-size: 52px;
    color: var(--logo-light);
  }
  .card--front .wordmark {
    position: absolute;
    top: 40px;
    left: 0;
    right: 0;
    justify-content: center;
    font-size: 46px;
    color: var(--ink-soft);
  }
  .holder {
    position: absolute;
    top: 160px;
    right: 370px;
    text-align: right;
  }
  .holder__name {
    font-family: "Oswald", sans-serif;
    font-weight: 600;
    font-size: 38px;
    line-height: 1;
    color: var(--brand-blue);
    letter-spacing: .5px;
  }
  .holder__role {
    margin-top: 8px;
    font-size: 17px;
    color: var(--ink-soft);
    letter-spacing: .5px;
  }
  .divider {
    position: absolute;
    top: 156px;
    left: 278px;
    width: 2px;
    height: 96px;
    background: var(--brand-blue);
  }
  .contact {
    position: absolute;
    top: 158px;
    left: 302px;
    margin: 0;
    padding: 0;
    list-style: none;
    font-size: 17px;
    letter-spacing: .8px;
    color: var(--ink);
  }
  .contact__item {
    display: flex;
    align-items: center;
    gap: 12px;
    height: 24px;
  }
  .contact__icon {
    width: 13px;
    height: 13px;
    fill: none;
    stroke: var(--brand-blue);
    stroke-width: 1.6;
  }
  .address {
    position: absolute;
    bottom: 34px;
    left: 0;
    right: 0;
    text-align: center;
    font-size: 17px;
    letter-spacing: .8px;
    color: var(--ink);
  }
</style>
</head>
<body>
<main class="stage">

  <section class="card card--back" aria-label="Card back">
    <div class="wordmark">
      <span class="wordmark__square"></span>
      <span class="wordmark__name">talvern &amp; co</span>
    </div>
  </section>

  <section class="card card--front" aria-label="Card front">
    <div class="wordmark">
      <span class="wordmark__square"></span>
      <span class="wordmark__name">talvern &amp; co</span>
    </div>

    <div class="holder">
      <div class="holder__name">DANIEL HART</div>
      <div class="holder__role">Director</div>
    </div>

    <div class="divider"></div>

    <ul class="contact">
      <li class="contact__item">
        <svg class="contact__icon" viewBox="0 0 14 14" aria-hidden="true"><path d="M3 1.5 L5.5 1.5 L6 4.5 L4.5 5.5 Q5.5 8.5 8.5 9.5 L9.5 8 L12.5 8.5 L12.5 11 Q12 12.5 10.5 12.5 Q2 11.5 1.5 3.5 Q1.5 1.8 3 1.5 Z"/></svg>
        <span>+612&nbsp;&nbsp;9470 3155</span>
      </li>
      <li class="contact__item">
        <svg class="contact__icon" viewBox="0 0 14 14" aria-hidden="true"><rect x="4" y="1.5" width="6" height="3.5"/><rect x="1.5" y="5" width="11" height="5"/><rect x="4" y="8.5" width="6" height="4"/></svg>
        <span>+612&nbsp;&nbsp;9470 3166</span>
      </li>
      <li class="contact__item">
        <svg class="contact__icon" viewBox="0 0 14 14" aria-hidden="true"><rect x="1.5" y="3" width="11" height="8"/><path d="M1.5 3 L7 8 L12.5 3"/></svg>
        <span>mail@tcpltd.com.au</span>
      </li>
      <li class="contact__item">
        <svg class="contact__icon" viewBox="0 0 14 14" aria-hidden="true"><circle cx="7" cy="7" r="5.5"/><ellipse cx="7" cy="7" rx="2.4" ry="5.5"/><path d="M1.5 7 H12.5 M2.5 4.2 H11.5 M2.5 9.8 H11.5"/></svg>
        <span>www.tcpltd.com.au</span>
      </li>
    </ul>

    <p class="address">40-48 Harrow Lane Sydney NSW 2000 Australia</p>
  </section>

</main>
</body>
</html>
```